Book Cover for Memoir: Sexual Assault and Traumatic Stress

I need a cover design for a memoir that is a victim's story of a sexual assault. I will need a print-on-demand cover, an eBook cover, and a 3D thumbnail image. The thumbnail and eBook cover will be used immediately, and the POD cover will be used in a few months with the full manuscript is ready. Therefore, I need an artist who is willing to make small adjustments if needed once the page count is set.

I have a image I have purchased that should give you an idea of the desired direction, but you can feel free to use your own images. I have attached some examples of book covers I like. I attached a color palette for fonts.

Overall Look: Fonts should be feminine and thin, but large to stand out. Look should be simple and elegant, and display and overall depressing feeling. There should be enough detail though to make it look professionally put together. Not TOO minimalistic.

I have also attached the Print Harbor templates if you choose to use those. If not, ensure there is an open place for the barcode on the bottom right.

Requirements
Must have
• Title: Beneath Quiet Rain
Subtitle: One Woman's Account of Fear, Guilt & Silence
Author: Dana Ruth Whitford
Audience: Mostly women 18-30
Quote (for the back): "I always thought I'd know how I'd react if I ever was raped. I was wrong. I've been wrong a lot lately."
Summary (back cover): When twenty-seven-year-old Dana Whitford wakes up with a gut-wrenching feeling, she has little memory of the horrifying events that occurred the night before. Days earlier, Dana was a spirited single mom who had abandoned her hometown to raise her daughter in the city and pursue her dreams. In the short months since Dana’s move to Seattle, she became the adored lover of a charismatic lawyer, started a new business, and finally felt life was going her way. So what happened to cause her to break?

In a gripping and heartbreaking narrative, Dana tells the true story of how her life unraveled from the traumatic events that took place that night and why what seems obvious to everyone else is impossible for Dana to believe. Beneath Quiet Rain is a chilling exploration of memory through trauma, trust in humanity, and a captivating story of strength and survival that appeals to the heart of fathers and mothers, sons and daughters, and men and women alike.
Nice to have
• BACK COVER: I'd like to have a photo on the back. This should depict the happy life of the main character before the sexual assault, and should be with her daughter. Or should be a nature scene that starts at the corner and blends into the rest of the cover. I have attached a possible image or you can use something you like.

```html
<!DOCTYPE html>
<html lang="en">
<head>
<meta charset="utf-8">
<title>Beneath Quiet Rain — Book Cover Wrap</title>
<link rel="stylesheet" href="https://fonts.googleapis.com/css2?family=Oranienbaum&family=PT+Serif&display=swap">
<style>
  :root {
    --red: #c8161d;
    --black: #0a0a0a;
    --white: #ffffff;
    --blurb-bg: #f3ddd3;
    --text-dark: #2a1e1a;
    --skin-light: #e9cfbf;
    --skin-mid: #c89c84;
    --skin-shadow: #8a6450;
    --hair-dark: #2b1c15;
    --sheet: #eeeae6;
  }
  * { margin: 0; padding: 0; box-sizing: border-box; }
  html, body { width: 1200px; height: 841px; overflow: hidden; background: var(--white); }
  .cover-wrap { position: relative; width: 1200px; height: 841px; overflow: hidden; }

  /* Back cover */
  .back-cover { position: absolute; left: 0; top: 0; width: 562px; height: 841px; }
  .back-photo {
    position: absolute; inset: 0;
    background:
      linear-gradient(180deg, rgba(60,40,30,0.45) 0%, rgba(60,40,30,0) 14%, rgba(238,234,230,0) 78%, rgba(238,234,230,0.85) 100%),
      linear-gradient(90deg, var(--hair-dark) 0%, #5e4232 8%, var(--skin-mid) 22%, var(--skin-light) 45%, #efd9cb 100%);
  }
  .back-quote {
    position: absolute; left: 62px; top: 350px; width: 400px;
    font-family: "Oranienbaum", "Times New Roman", serif;
    font-size: 19px; line-height: 28px; color: var(--red);
  }
  .blurb-box {
    position: absolute; left: 42px; top: 432px; width: 220px; height: 371px;
    background: var(--blurb-bg); border-radius: 12px;
    padding: 16px 14px 10px 18px;
  }
  .blurb-text {
    font-family: "PT Serif", Georgia, serif; font-size: 12.2px; line-height: 20px;
    color: var(--text-dark); text-align: justify; hyphens: auto;
  }
  .drop-cap {
    float: left; font-size: 46px; line-height: 36px; color: var(--red);
    margin: 2px 3px 0 0; font-family: "Oranienbaum", "Times New Roman", serif;
  }
  .barcode-space {
    position: absolute; left: 313px; top: 690px; width: 213px; height: 113px;
    background: var(--white);
  }

  /* Spine */
  .spine { position: absolute; left: 562px; top: 0; width: 78px; height: 841px; background: var(--black); }
  .spine-photo {
    position: absolute; left: 13px; top: 6px; width: 52px; height: 134px;
    background: linear-gradient(180deg, var(--black) 0%, var(--hair-dark) 25%, var(--skin-mid) 55%, var(--skin-light) 85%, var(--black) 100%);
  }
  .spine-author {
    position: absolute; left: 0; top: 150px; width: 78px; text-align: center;
    font-family: "Oranienbaum", "Times New Roman", serif; font-size: 22px; line-height: 25px; color: var(--white);
  }
  .spine-title {
    position: absolute; left: 0; top: 428px; width: 78px; height: 380px;
    display: flex; justify-content: flex-start; align-items: center;
    writing-mode: vertical-rl;
    font-family: "Oranienbaum", "Times New Roman", serif; font-size: 46px; line-height: 78px; color: var(--black);
    -webkit-text-stroke: 1.4px var(--red);
    white-space: nowrap;
  }

  /* Front cover */
  .front-cover { position: absolute; left: 640px; top: 0; width: 560px; height: 841px; }
  .front-photo {
    position: absolute; inset: 0;
    background:
      linear-gradient(180deg, rgba(50,32,24,0.55) 0%, rgba(50,32,24,0) 16%, rgba(238,234,230,0) 80%, rgba(238,234,230,0.8) 100%),
      linear-gradient(90deg, #a07a64 0%, var(--skin-light) 22%, #dcbba7 48%, var(--skin-shadow) 72%, #4a3024 88%, var(--hair-dark) 100%);
  }
  .front-subtitle {
    position: absolute; right: 38px; top: 40px; text-align: right;
    font-family: "Oranienbaum", "Times New Roman", serif;
    font-size: 38px; line-height: 47px; color: var(--red);
  }
  .front-author {
    position: absolute; right: 38px; top: 562px;
    font-family: "Oranienbaum", "Times New Roman", serif; font-size: 40px; line-height: 48px; color: var(--white);
  }
  .front-title {
    position: absolute; right: 38px; top: 620px; text-align: right;
    font-family: "Oranienbaum", "Times New Roman", serif; font-size: 104px; line-height: 92px;
    color: var(--black); -webkit-text-stroke: 1.6px var(--red);
    white-space: nowrap;
  }
</style>
</head>
<body>
<main class="cover-wrap">
  <section class="back-cover">
    <div class="back-photo" role="img" aria-label="Close-up portrait photograph of a young woman with brown eyes, soft skin tones and dark hair"></div>
    <p class="back-quote">“I always thought I’d know how I’d react if I ever was raped.<br>I was wrong. I’ve been wrong a lot lately.”</p>
    <div class="blurb-box">
      <p class="blurb-text"><span class="drop-cap">W</span>hen twenty-seven-year-old Dana Whitford wakes up with a gut-wrenching feeling, she has little memory of the horrifying events that occurred the night before. Days earlier, Dana was a spirited single mom who had abandoned her hometown to raise her daughter in the city and pursue her dreams. In the short months since Dana’s move to Seattle, she became the adored lover of a charismatic lawyer, started a new business, and finally felt life was going her way. So what happened to cause her to break?</p>
    </div>
    <div class="barcode-space"></div>
  </section>

  <section class="spine">
    <div class="spine-photo" role="img" aria-label="Small photograph of a woman hugging her knees with her head bowed"></div>
    <p class="spine-author">Dana<br>Ruth<br>Whitford</p>
    <h2 class="spine-title">Beneath Quiet Rain</h2>
  </section>

  <section class="front-cover">
    <div class="front-photo" role="img" aria-label="Photograph of a woman sitting hunched, arms around her knees and head bowed, over a close-up portrait of a woman's eyes"></div>
    <p class="front-subtitle">One Woman’s<br>Account of Fear,<br>Guilt &amp; Silence</p>
    <p class="front-author">Dana Ruth Whitford</p>
    <h1 class="front-title">Beneath<br>Quiet Rain</h1>
  </section>
</main>
</body>
</html>
```